Consultative Employee Benifits Firm Needs Business Card Design Project

We need a business card design for a new company based in Northern Virginia called "Tallow Ridge Advisors, LLC. We are both a wealth management advisory firm, as well as an employee benefits firm, which strives to provide superior creativity in employee benefits plan design and greater client and employee satisfaction. We are obsessed with service and follow up.

Our firm specializes in the areas of group health, life, dental, disability, voluntary benefits, Executive Benefits, HRA and HSA programs. We offer competitive employee benefit packages and pricing models for single or multi-state/multi location companies by maintaining preferred relationships with a large number of regional and national carriers.

Our firm also considers the many dimensions of your wealth through an integrated process we call wealth structuring — a comprehensive, dynamic approach to building, preserving, enjoying and transferring your wealth. And because we are often dealing with complex ownership structures and complicated, changing family dynamics, we bring the highest level of experience and creativity to managing your wealth. We work hard to help ensure that your legacy lasts by preparing your children for the financial challenges and opportunities that are headed their way.

Our final design should communicate an integrated approach to finanial safety and optimization
Updates

 Due to a few designers not accepting due to low budget, I have increased budget payout 19%. 

Project Deadline Extended
Reason: I have only heard from 12 designers. So, maybe I did not give the right amount of time to do the project. For the designers that have submitted their designs, thank you. I have seen three or four designs that I liked and might end up with one of them after it's all over, but I thought I would see between 20 - 25 before everything was over. Dean

Target Market(s)

Professionals; doctors, contractors, small to mid size business owners, ages 50 -65 with nert worth of 2MM

Industry/Entity Type

Financial

Requirements
Must have
• Tallow Ridge Advisors, LLC

Dean Harlow
President
17459 Marrowind Lane Street
Quenby Hollow, 20418

Office: 703 562-1094
Cell: 703 817-2650
Fax: 703 275-6831
Email: deanharlow@mailtrove.net
Should not have
• No pink or yellow colors.
No generic clipart (coins, dollar signs, money bags, graphs)

```html
<!DOCTYPE html>
<html lang="en">
<head>
<meta charset="utf-8">
<title>Tallow Ridge Advisors, LLC — Business Card</title>
<link rel="stylesheet" href="https://fonts.googleapis.com/css2?family=Tinos:wght@400;700&display=swap">
<style>
  :root {
    --navy: #0c3562;
    --navy-soft: #174a7e;
    --sky: #29a8e0;
    --paper: #ffffff;
    --stage: #eceef0;
    --ink-light: #ffffff;
  }
  * { margin: 0; padding: 0; box-sizing: border-box; }
  html, body { width: 1200px; height: 1200px; overflow: hidden; }
  body {
    background: var(--stage);
    font-family: "Tinos", "Times New Roman", serif;
    position: relative;
  }
  .card {
    position: absolute;
    top: 430px;
    width: 560px;
    height: 340px;
    overflow: hidden;
    box-shadow: 0 2px 6px rgba(0,0,0,0.12);
  }
  /* Front */
  .card-front { left: 30px; background: var(--paper); }
  .brand {
    position: absolute;
    left: 70px;
    top: 40px;
    display: flex;
    align-items: center;
    gap: 22px;
  }
  .brand-dot {
    width: 84px; height: 84px;
    border-radius: 50%;
    background: var(--navy);
    flex: none;
  }
  .brand-name {
    color: var(--navy);
    font-weight: 700;
    text-transform: uppercase;
    line-height: 1;
  }
  .brand-name .line-main { display: block; font-size: 34px; letter-spacing: 0.5px; }
  .brand-name .line-sub { display: block; font-size: 19px; letter-spacing: 1px; margin-top: 8px; text-align: center; }

  .front-lower {
    position: absolute;
    left: 0; right: 0; bottom: 0;
    height: 155px;
  }
  .accent-strip {
    position: absolute;
    left: 0; top: 0; bottom: 0;
    width: 26px;
    background: var(--sky);
  }
  .person {
    position: absolute;
    left: 46px;
    top: 22px;
    color: var(--navy);
  }
  .person-name { font-size: 25px; font-weight: 700; text-transform: uppercase; letter-spacing: 0.5px; }
  .person-title { font-size: 13px; font-weight: 700; text-transform: uppercase; margin: 2px 0 0 24px; letter-spacing: 0.5px; }
  .person-address { font-size: 14.5px; font-weight: 700; line-height: 1.45; margin-top: 16px; }

  .contact-panel {
    position: absolute;
    left: 320px; right: 0; top: 0; bottom: 0;
    background: var(--navy);
    color: var(--ink-light);
    text-align: right;
    padding: 46px 16px 0 0;
    font-size: 15px;
    line-height: 1.5;
  }

  /* Back */
  .card-back { left: 610px; background: var(--navy); }
  .back-circle {
    position: absolute;
    left: 70px; top: -20px;
    width: 300px; height: 300px;
    border-radius: 50%;
    background: var(--navy-soft);
  }
  .name-band {
    position: absolute;
    left: 0; right: 0;
    top: 254px;
    height: 54px;
    background: var(--sky);
    color: var(--ink-light);
    text-align: center;
    text-transform: uppercase;
    font-weight: 700;
    line-height: 1;
    padding-top: 8px;
  }
  .name-band .line-main { display: block; font-size: 24px; letter-spacing: 0.5px; }
  .name-band .line-sub { display: block; font-size: 13px; letter-spacing: 1px; margin-top: 4px; }
</style>
</head>
<body>
  <section class="card card-front" aria-label="Card front">
    <div class="brand">
      <span class="brand-dot"></span>
      <div class="brand-name">
        <span class="line-main">Tallow Ridge</span>
        <span class="line-sub">Advisors, LLC</span>
      </div>
    </div>
    <div class="front-lower">
      <div class="accent-strip"></div>
      <div class="person">
        <p class="person-name">Dean Harlow</p>
        <p class="person-title">President</p>
        <p class="person-address">17459 Marrowind Lane Street<br>Quenby Hollow, 20418</p>
      </div>
      <div class="contact-panel">
        <p>Office: 703 562-1094</p>
        <p>Cell: 703 817-2650</p>
        <p>Fax: 703 275-6831</p>
        <p>Email: deanharlow@mailtrove.net</p>
      </div>
    </div>
  </section>

  <section class="card card-back" aria-label="Card back">
    <div class="back-circle"></div>
    <div class="name-band">
      <span class="line-main">Tallow Ridge</span>
      <span class="line-sub">Advisors, LLC</span>
    </div>
  </section>
</body>
</html>
```